Tamarack Hearth Partners Business Card

Looking for a new business card layout. We are a real estate firm w/ a logo, old design attached. Must keep the same elements on there, just need a fresh look and possible some foil accents. Looking for a simpler design w/ more modern style.

Target Market(s)

Real Estate clients

Industry/Entity Type

Real Estate Agent

Contact Information for Business Card

see attached

Font styles to use
Sans Serif

Requirements
Must have
• all elements on current biz card
Nice to have
• modern look, simpler than we have!
Should not have
• no serif fonts

```html
<!DOCTYPE html>
<html lang="en">
<head>
<meta charset="utf-8">
<title>Tamarack Hearth Partners Business Card</title>
<link href="https://fonts.googleapis.com/css2?family=Lato:wght@400;700&display=swap" rel="stylesheet">
<style>
  :root {
    --teal: #12bccb;
    --teal-deep: #3aaeb0;
    --ink-gray: #7a7a7a;
    --card: #ffffff;
    --backdrop: #f0f1f2;
  }
  * { margin: 0; padding: 0; box-sizing: border-box; }
  html, body {
    width: 1200px; height: 1200px; overflow: hidden;
    background: var(--backdrop);
    font-family: "Lato", "Helvetica Neue", Arial, sans-serif;
  }
  .card {
    position: absolute;
    background: var(--card);
  }
  .card--front { left: 222px; top: 122px; width: 798px; height: 461px; }
  .card--back  { left: 223px; top: 660px; width: 795px; height: 454px; }

  .brand-name {
    position: absolute;
    font-weight: 700;
    color: var(--teal);
    text-transform: uppercase;
    line-height: 1.05;
    letter-spacing: 0.02em;
  }
  .card--front .brand-name { left: 56px; top: 54px; font-size: 34px; }
  .card--back .brand-name {
    left: 0; right: 0; top: 178px;
    text-align: center; font-size: 48px;
    color: var(--teal-deep);
  }

  .agent-photo {
    position: absolute;
    left: 598px; top: 54px; width: 142px; height: 171px;
    border: 3px solid var(--teal);
    background: linear-gradient(160deg, #d9c9b6 0%, #e8dccb 45%, #3fc0c6 100%);
  }

  .agent-line {
    position: absolute;
    left: 56px; top: 274px;
    display: flex; align-items: baseline;
  }
  .agent-name {
    font-size: 38px; font-weight: 700;
    color: var(--teal); letter-spacing: 0.04em;
  }
  .agent-title {
    font-size: 21px; color: var(--ink-gray);
    letter-spacing: 0.08em; margin-left: 2px;
  }
  .agent-rule {
    position: absolute;
    left: 56px; top: 330px; width: 684px; height: 3px;
    background: var(--teal);
  }

  .contact-row {
    position: absolute;
    left: 56px; width: 684px;
    display: flex; justify-content: space-between;
    font-size: 20px; color: var(--ink-gray);
    white-space: nowrap;
  }
  .contact-row--top { top: 348px; }
  .contact-row--bottom { top: 388px; justify-content: flex-start; }
  .sep { color: var(--teal); font-weight: 700; margin: 0 10px; }
</style>
</head>
<body>
  <section class="card card--front">
    <div class="brand-name">Tamarack Hearth<br>Partners</div>
    <div class="agent-photo" role="img" aria-label="Portrait photo of the broker"></div>
    <div class="agent-line">
      <span class="agent-name">DANA WHITFIELD.</span>
      <span class="agent-title">PRINCIPAL BROKER</span>
    </div>
    <div class="agent-rule"></div>
    <div class="contact-row contact-row--top">
      <span>Cell: 541 555 0148</span><span class="sep">|</span>
      <span>Office: 541 555 0172</span><span class="sep">|</span>
      <span>E: dana@hearthkeys.com</span>
    </div>
    <div class="contact-row contact-row--bottom">
      <span>210 NW Juniper Ave Sisters, OR 97759</span><span class="sep">|</span>
      <span>TamarackHearth-Homes.com</span>
    </div>
  </section>

  <section class="card card--back">
    <div class="brand-name">Tamarack Hearth<br>Partners</div>
  </section>
</body>
</html>
```